Road Construction Company needs business cards

We would like a new business card designed for our business.

We're a road construction company based in Qld, Australia.

Can the business card please have the following information on it.

Name: Brent Malvoy
Position: General Manager
Phone: 0471 592 304
Email: Brent.malvoy@quendix.com.au
Address: 87 Harrowgate Ave, Pindarra, QLD, 4000
Website: www.quendix.com.au

Visually we'd like the card to be professional and simple.

Attached is our logo.

Our website is www.quendix.com.au

Target Market(s)

Men aged 25-60

Contact Information for Business Card

As listed in project description

Font styles to use
Serif

Requirements
Must have
• Large logo on back of card

```html
<!DOCTYPE html>
<html lang="en">
<head>
<meta charset="utf-8">
<title>Quendix Business Card</title>
<link rel="stylesheet" href="https://fonts.googleapis.com/css2?family=Michroma&family=Open+Sans:wght@400;600;800&display=swap">
<style>
  :root {
    --backdrop: #2b2b2b;
    --brand-blue: #0455a4;
    --sky-blue: #3a9ad9;
    --ink: #1c1c1c;
    --paper: #ffffff;
    --rule: #b9b9b9;
  }
  * { margin: 0; padding: 0; box-sizing: border-box; }
  html, body {
    width: 1200px; height: 689px; overflow: hidden;
    background: var(--backdrop);
    font-family: "Open Sans", sans-serif;
  }
  .canvas { position: relative; width: 1200px; height: 689px; }

  .card {
    position: absolute; top: 190px;
    width: 540px; height: 309px;
    border-radius: 22px; overflow: hidden;
    box-shadow: 0 14px 30px rgba(0,0,0,0.45);
  }
  .card-back { left: 40px; background: var(--brand-blue); }
  .card-front { left: 620px; background: var(--paper); }

  .wordmark {
    display: flex; align-items: center; gap: 12px;
    font-family: "Open Sans", sans-serif; font-weight: 800;
    letter-spacing: 4px; line-height: 1;
  }
  .wordmark-mark { display: block; width: 18px; height: 18px; }
  .card-back .wordmark {
    position: absolute; left: 0; right: 0; top: 50%;
    transform: translateY(-50%); justify-content: center;
    font-size: 58px; color: var(--paper);
  }
  .card-back .wordmark-mark { width: 22px; height: 22px; background: var(--sky-blue); }

  .card-front .wordmark {
    position: absolute; left: 34px; top: 148px;
    font-size: 38px; color: var(--brand-blue);
  }
  .card-front .wordmark-mark { background: var(--sky-blue); }

  .divider {
    position: absolute; left: 278px; top: 28px; width: 1px; height: 200px;
    background: linear-gradient(to bottom, transparent, var(--rule) 30%, var(--rule) 70%, transparent);
  }

  .contact-block { position: absolute; left: 300px; top: 46px; right: 18px; }
  .person-name {
    font-family: "Michroma", sans-serif; font-size: 17px;
    color: var(--brand-blue); letter-spacing: 1px; line-height: 1.2;
    text-transform: uppercase;
  }
  .person-role { font-size: 14px; color: var(--sky-blue); margin-top: 2px; }
  .contact-list { list-style: none; margin-top: 12px; }
  .contact-list li {
    display: flex; align-items: center; gap: 8px;
    font-size: 11.5px; color: var(--ink); line-height: 21px; white-space: nowrap;
  }
  .contact-list svg { width: 13px; height: 13px; flex: none; fill: var(--brand-blue); }
  .web-accent { color: var(--brand-blue); }
  .address { margin-top: 10px; font-size: 12px; line-height: 19px; color: var(--ink); padding-left: 21px; }

  .edge-line { position: absolute; left: 0; right: 0; bottom: 32px; height: 4px; background: var(--sky-blue); }
  .edge-band { position: absolute; left: 0; right: 0; bottom: 0; height: 26px; background: var(--brand-blue); }
</style>
</head>
<body>
<main class="canvas">

  <section class="card card-back" aria-label="Card back">
    <div class="wordmark"><span class="wordmark-mark"></span>QUENDIX</div>
  </section>

  <section class="card card-front" aria-label="Card front">
    <div class="wordmark"><span class="wordmark-mark"></span>QUENDIX</div>
    <div class="divider"></div>

    <div class="contact-block">
      <h1 class="person-name">Brent Malvoy</h1>
      <p class="person-role">General Manager</p>
      <ul class="contact-list">
        <li>
          <svg viewBox="0 0 24 24" aria-hidden="true"><path d="M6.6 10.8a15.1 15.1 0 0 0 6.6 6.6l2.2-2.2a1 1 0 0 1 1-.25 11.4 11.4 0 0 0 3.6.57 1 1 0 0 1 1 1V20a1 1 0 0 1-1 1A17 17 0 0 1 3 4a1 1 0 0 1 1-1h3.5a1 1 0 0 1 1 1c0 1.25.2 2.45.57 3.57a1 1 0 0 1-.25 1z"/></svg>
          0471 592 304
        </li>
        <li>
          <svg viewBox="0 0 24 24" aria-hidden="true"><path d="M2 5h20v14H2z" fill="none"/><path d="M2 5h20v14H2V5zm2 2v.5l8 5 8-5V7H4z"/></svg>
          Brent.malvoy@quendix.com.au
        </li>
        <li>
          <svg viewBox="0 0 24 24" aria-hidden="true"><path d="M12 2a10 10 0 1 0 0 20 10 10 0 0 0 0-20zm6.9 6h-3a15.7 15.7 0 0 0-1.3-3.9A8 8 0 0 1 18.9 8zM12 4c.8 1.2 1.5 2.5 1.9 4h-3.8c.4-1.5 1.1-2.8 1.9-4zM4.3 14a8 8 0 0 1 0-4h3.4a16 16 0 0 0 0 4H4.3zm.8 2h3a15.7 15.7 0 0 0 1.3 3.9A8 8 0 0 1 5.1 16zm3-8h-3a8 8 0 0 1 4.3-3.9A15.7 15.7 0 0 0 8.1 8zM12 20c-.8-1.2-1.5-2.5-1.9-4h3.8c-.4 1.5-1.1 2.8-1.9 4zm2.3-6H9.7a14 14 0 0 1 0-4h4.6a14 14 0 0 1 0 4zm.3 5.9a15.7 15.7 0 0 0 1.3-3.9h3a8 8 0 0 1-4.3 3.9zm1.7-5.9a16 16 0 0 0 0-4h3.4a8 8 0 0 1 0 4h-3.4z"/></svg>
          <span>www.<span class="web-accent">quendix</span>.com.au</span>
        </li>
      </ul>
      <p class="address">87 Harrowgate Ave<br>Pindarra, QLD, 4000</p>
    </div>

    <div class="edge-line"></div>
    <div class="edge-band"></div>
  </section>

</main>
</body>
</html>
```